Welding company needs a business card

We are looking for a logo and business card.

Contact Information for Business Card

418 Cobblestone Lane
York, PA 17402
410-555-0173
Rmfabworksco@quorvamail.com

```html
<!DOCTYPE html>
<html lang="en">
<head>
<meta charset="utf-8">
<title>RM Fabworks — Business Card</title>
<link rel="stylesheet" href="https://fonts.googleapis.com/css2?family=Arimo:wght@700&family=Montserrat:wght@400&display=swap">
<style>
  :root {
    --stage: #1e5150;
    --paper: #ffffff;
    --teal-deep: #2f9a9c;
    --teal: #45b4c4;
    --sky: #8fd6e3;
    --mist: #e9f3ef;
    --lemon: #ece483;
    --ink-brown: #6f5a43;
    --mark-teal: #3fb2b5;
  }
  * { margin: 0; padding: 0; box-sizing: border-box; }
  html, body { width: 1200px; height: 927px; overflow: hidden; }
  body { background: var(--stage); position: relative; font-family: "Arimo", Arial, sans-serif; }

  .card { position: absolute; width: 614px; height: 368px; }

  /* Front */
  .card--front { left: 45px; top: 61px; background: var(--paper); }
  .card__wash {
    position: absolute; left: 20px; top: 21px; width: 573px; height: 327px;
    background:
      radial-gradient(ellipse 45% 55% at 92% 8%, var(--lemon) 0%, transparent 70%),
      radial-gradient(ellipse 35% 45% at 72% 30%, var(--mist) 0%, transparent 75%),
      radial-gradient(ellipse 30% 45% at 82% 75%, #dcefe6 0%, transparent 75%),
      radial-gradient(ellipse 45% 55% at 12% 15%, var(--sky) 0%, transparent 75%),
      radial-gradient(ellipse 50% 50% at 30% 80%, var(--teal-deep) 0%, transparent 75%),
      linear-gradient(120deg, var(--teal) 0%, #58c0cc 50%, #b9e2dd 100%);
  }

  /* Back */
  .card--back {
    left: 526px; top: 511px;
    background:
      radial-gradient(ellipse 40% 60% at 100% 0%, var(--lemon) 0%, transparent 70%),
      radial-gradient(ellipse 30% 40% at 82% 100%, #d9efea 0%, transparent 75%),
      linear-gradient(100deg, var(--teal) 0%, var(--teal-deep) 40%, #5fbcc0 70%, #dcefe0 100%);
  }
  .card__face {
    position: absolute; left: 21px; top: 19px; width: 573px; height: 328px;
    background: var(--paper);
  }

  .brand {
    position: absolute; display: flex; align-items: center; gap: 8px;
    font-family: "Montserrat", Arial, sans-serif; font-weight: 400;
    letter-spacing: 0.14em; white-space: nowrap;
  }
  .brand__dot { width: 12px; height: 12px; border-radius: 50%; background: currentColor; }
  .brand--front { left: 307px; top: 235px; transform: translate(-50%, -50%); color: var(--paper); font-size: 20px; }
  .brand--back { left: 457px; top: 77px; transform: translate(-50%, -50%); color: var(--mark-teal); font-size: 17px; }

  .contact { color: var(--ink-brown); font-weight: 700; }
  .contact__email {
    position: absolute; left: 24px; top: 290px;
    transform-origin: 0 0; transform: rotate(-90deg);
    font-size: 16px; white-space: nowrap;
  }
  .contact__email .label { margin-right: 12px; }
  .contact__list {
    position: absolute; left: 383px; top: 219px;
    font-size: 18px; line-height: 22.5px; list-style: none;
  }
  .contact__list li { display: grid; grid-template-columns: 26px auto; }
  .contact__list .sub { font-size: 17px; }
</style>
</head>
<body>
  <section class="card card--front" aria-label="Business card front">
    <div class="card__wash"></div>
    <div class="brand brand--front"><span class="brand__dot"></span>RM FABWORKS</div>
  </section>

  <section class="card card--back" aria-label="Business card back">
    <div class="card__face">
      <div class="brand brand--back"><span class="brand__dot"></span>RM FABWORKS</div>
      <p class="contact contact__email"><span class="label">E</span>Rmfabworksco@quorvamail.com</p>
      <ul class="contact contact__list">
        <li><span>M</span><span>410-555-0173</span></li>
        <li><span>A</span><span class="sub">418 Cobblestone Lane</span></li>
        <li><span></span><span class="sub">York, PA 17402</span></li>
      </ul>
    </div>
  </section>
</body>
</html>
```